Sunridge Pilates Centre
Business Cards
Bright & Fun-filled
Maribel Foster
Owner/Certified Pilates Instructor
2847 Kestrel Dr La Mesa CA 91873
n/A
do not have until sept 20
maribel@sunridgepilatescentre.com
www.sunridgepilatescentre.com
not sure but maybe? maybe logo or a Konrad Weller Quote or??

```html
<!DOCTYPE html>
<html lang="en">
<head>
<meta charset="utf-8">
<title>Sunridge Pilates Centre – Stationery</title>
<link href="https://fonts.googleapis.com/css2?family=Open+Sans:wght@400;600&display=swap" rel="stylesheet">
<style>
:root{
  --bg:#ededed;
  --paper:#ffffff;
  --gold:#c49a3c;
  --gold-light:#e3c27a;
  --gold-dark:#a57a25;
  --ink:#555555;
  --ink-soft:#8a8a8a;
}
*{box-sizing:border-box;margin:0;padding:0}
html,body{width:1200px;height:936px;overflow:hidden}
body{background:var(--bg);font-family:"Open Sans",Arial,sans-serif;color:var(--ink);position:relative}
.piece{position:absolute;background:var(--paper);overflow:hidden}
.wave{position:absolute;left:0;bottom:0;width:100%;display:block}

.brand{display:flex;align-items:center;gap:8px;color:var(--gold);font-weight:600;line-height:1.1}
.brand-dot{flex:none;border-radius:50%;border:2px solid var(--gold)}

/* letterhead */
.letterhead{left:38px;top:30px;width:530px;height:660px}
.letterhead .brand{position:absolute;left:44px;top:40px;font-size:17px}
.letterhead .brand-dot{width:30px;height:30px}
.contact{position:absolute;right:40px;top:38px;font-size:8px;line-height:15px;color:var(--ink-soft)}
.contact li{list-style:none;display:flex;align-items:center;gap:5px}
.contact svg{width:8px;height:8px;fill:var(--gold)}
.letter-body{position:absolute;left:44px;top:150px;width:420px;font-size:7.5px;line-height:12px;color:var(--ink-soft)}
.letter-body p{margin-bottom:11px}
.signature{display:block;width:60px;height:20px;background:linear-gradient(90deg,#d9d9d9,#efefef);border-radius:3px;margin:6px 0 6px}
.signer{font-weight:600;color:var(--ink)}

/* folder */
.folder{left:633px;top:30px;width:530px;height:660px}
.folder .brand{position:absolute;left:0;right:0;top:170px;justify-content:center;font-size:30px;text-align:center}
.folder .brand-dot{width:46px;height:46px;border-width:3px}

/* business cards */
.card{left:38px;width:185px;height:104px}
.card-front{top:708px}
.card-back{top:824px}
.card .brand{font-size:9.5px;gap:5px}
.card .brand-dot{width:14px;height:14px;border-width:1.5px}
.card-front .brand{position:absolute;left:12px;top:10px}
.card-front .details{position:absolute;right:10px;top:36px;text-align:right;font-size:5px;line-height:7px;color:var(--ink-soft)}
.card-front .details strong{display:block;font-size:6.5px;line-height:9px;color:var(--ink);font-weight:600}
.card-back .brand{position:absolute;left:0;right:0;top:18px;justify-content:center}
.card-back .web{position:absolute;left:0;right:0;top:46px;text-align:center;font-size:5.5px;color:var(--ink-soft)}

/* envelopes */
.envelope{top:708px;height:180px}
.envelope-front{left:260px;width:340px}
.envelope-front .brand{position:absolute;left:22px;top:20px;font-size:12px;gap:6px}
.envelope-front .brand-dot{width:20px;height:20px}
.envelope-front .return{position:absolute;left:22px;top:66px;font-size:6px;line-height:9px;color:var(--ink-soft)}
.envelope-back{left:633px;width:530px}
.flap{position:absolute;left:0;top:0;width:100%;height:100%}
.envelope-back .web{position:absolute;left:0;right:0;top:34px;text-align:center;font-size:11px;letter-spacing:2px;color:#fff;font-weight:600}
</style>
</head>
<body>

<svg width="0" height="0" style="position:absolute">
  <defs>
    <linearGradient id="goldFill" x1="0" y1="0" x2="1" y2="1">
      <stop offset="0" stop-color="#e3c27a"/>
      <stop offset="0.5" stop-color="#c49a3c"/>
      <stop offset="1" stop-color="#a57a25"/>
    </linearGradient>
  </defs>
</svg>

<!-- letterhead -->
<section class="piece letterhead">
  <div class="brand"><span class="brand-dot"></span><span>Sunridge<br>Pilates Centre</span></div>
  <ul class="contact">
    <li><svg viewBox="0 0 10 10"><path d="M2 0h2l1 3-1.5 1a6 6 0 0 0 2.5 2.5L7 5l3 1v2a2 2 0 0 1-2 2A8 8 0 0 1 0 2a2 2 0 0 1 2-2z"/></svg>(619) 555-0142</li>
    <li><svg viewBox="0 0 10 10"><path d="M5 0a3.5 3.5 0 0 1 3.5 3.5C8.5 6 5 10 5 10S1.5 6 1.5 3.5A3.5 3.5 0 0 1 5 0zm0 2a1.5 1.5 0 1 0 0 3 1.5 1.5 0 0 0 0-3z"/></svg>2847 Kestrel Dr, La Mesa CA 91873</li>
    <li><svg viewBox="0 0 10 10"><path d="M0 2h10v6H0zM0 2l5 3.5L10 2" /></svg>maribel@sunridgepilatescentre.com</li>
    <li><svg viewBox="0 0 10 10"><circle cx="5" cy="5" r="5"/></svg>www.sunridgepilatescentre.com</li>
  </ul>
  <div class="letter-body">
    <p>June 4, 2024</p>
    <p>Dear Client,</p>
    <p>Thank you for choosing our studio. Our classes build strength, balance and calm through mindful movement, guided by certified instructors who tailor every session to your own pace and goals.</p>
    <p>We offer mat and reformer sessions for all levels, from first steps to advanced practice, in a bright and welcoming space.</p>
    <p>We look forward to seeing you on the mat soon and helping you feel your very best.</p>
    <p>Best Regards,</p>
    <span class="signature" role="img" aria-label="handwritten signature"></span>
    <span class="signer">Maribel Foster</span><br>Owner
  </div>
  <svg class="wave" viewBox="0 0 530 170" preserveAspectRatio="none" height="170">
    <path d="M0 50 C150 -10 330 120 530 25" fill="none" stroke="var(--gold)" stroke-width="2"/>
    <path d="M0 72 C150 12 330 140 530 46 L530 170 L0 170Z" fill="url(#goldFill)"/>
  </svg>
</section>

<!-- presentation folder -->
<section class="piece folder">
  <div class="brand"><span class="brand-dot"></span><span>Sunridge<br>Pilates Centre</span></div>
  <svg class="wave" viewBox="0 0 530 220" preserveAspectRatio="none" height="220">
    <path d="M0 75 C160 5 330 150 530 30" fill="none" stroke="var(--gold)" stroke-width="2.5"/>
    <path d="M0 100 C160 30 330 175 530 55 L530 220 L0 220Z" fill="url(#goldFill)"/>
  </svg>
</section>

<!-- business cards -->
<section class="piece card card-front">
  <div class="brand"><span class="brand-dot"></span><span>Sunridge<br>Pilates Centre</span></div>
  <div class="details">
    <strong>Maribel Foster</strong>
    Owner/Certified Pilates Instructor<br>
    (619) 555-0142<br>
    2847 Kestrel Dr La Mesa CA 91873<br>
    maribel@sunridgepilatescentre.com
  </div>
  <svg class="wave" viewBox="0 0 185 40" preserveAspectRatio="none" height="24">
    <path d="M0 12 C55 -4 120 30 185 6" fill="none" stroke="var(--gold)" stroke-width="1"/>
    <path d="M0 20 C55 4 120 38 185 14 L185 40 L0 40Z" fill="url(#goldFill)"/>
  </svg>
</section>

<section class="piece card card-back">
  <div class="brand"><span class="brand-dot"></span><span>Sunridge Pilates Centre</span></div>
  <div class="web">www.sunridgepilatescentre.com</div>
  <svg class="wave" viewBox="0 0 185 40" preserveAspectRatio="none" height="32">
    <path d="M0 12 C55 -4 120 30 185 6" fill="none" stroke="var(--gold)" stroke-width="1"/>
    <path d="M0 20 C55 4 120 38 185 14 L185 40 L0 40Z" fill="url(#goldFill)"/>
  </svg>
</section>

<!-- envelope front -->
<section class="piece envelope envelope-front">
  <div class="brand"><span class="brand-dot"></span><span>Sunridge<br>Pilates Centre</span></div>
  <p class="return">2847 Kestrel Dr<br>La Mesa CA 91873</p>
</section>

<!-- envelope back -->
<section class="piece envelope envelope-back">
  <svg class="flap" viewBox="0 0 530 180" preserveAspectRatio="none">
    <path d="M0 0 H530 V60 C340 130 190 20 0 85Z" fill="url(#goldFill)"/>
    <path d="M0 95 C190 30 340 140 530 70" fill="none" stroke="var(--gold)" stroke-width="1.5"/>
  </svg>
  <div class="web">www.sunridgepilatescentre.com</div>
</section>

</body>
</html>
```